Healthcare technology company needs website design

We need a logo for a new company based in the U.S. We develop software to assist consumers identifying lowest cost healthcare coverage methods, including insurance, discount cards, and cash options. We would like to see designs that use multiple shades of green with the optional addition of other complimentary colors. The final design should communicate a unique blend of saving money while receiving the healthcare you need.
Need the following pages/sections: Homepage, Solutions, About Us, Contact
Competitors: www.velorimed.example; www.qzplo.example

Target Market(s)

Businesses

Industry/Entity Type

Healthcare

Coding

Coded - Design and coding required

Number of Pages Required

4 page

Colors
0054AA
0677BA
7BADD7
CADEEF
E8F1F8
00AB8E
00BBA5
67D7C9
C6EFE9
E9F9F6

Requirements
Must have
• Matching color theme with logo
Nice to have
• Animated background

```html
<!DOCTYPE html>
<html lang="en">
<head>
<meta charset="utf-8">
<title>Fernpath Health — Healthcare Software Solutions</title>
<link href="https://fonts.googleapis.com/css2?family=Montserrat:wght@400;500;600;700;800&display=swap" rel="stylesheet">
<style>
:root{
  --green:#00AB8E;
  --teal:#00BBA5;
  --mint:#E9F9F6;
  --ink:#0d1b22;
  --body:#4a5257;
  --line:#c9cfd2;
  --hero-dark:#0f2a33;
  --hero-mid:#24495a;
  --white:#ffffff;
}
*{box-sizing:border-box;margin:0;padding:0}
html,body{width:1200px;height:2484px;overflow:hidden}
body{font-family:"Montserrat",sans-serif;color:var(--ink);background:var(--white);position:relative}
.abs{position:absolute}
.hero{left:0;top:0;width:1200px;height:640px;background:radial-gradient(ellipse at 75% 40%,#3d6475 0%,var(--hero-mid) 35%,var(--hero-dark) 85%)}
.brand{left:141px;top:46px;display:flex;align-items:center;gap:12px;color:var(--green);font-weight:700;font-size:25px;letter-spacing:1px}
.brand-dot{width:34px;height:34px;border-radius:50%;background:var(--green)}
.nav{top:54px;right:148px;display:flex;align-items:center;gap:34px}
.nav a{color:var(--white);font-weight:700;font-size:13px;text-decoration:none}
.btn{display:inline-flex;align-items:center;justify-content:center;background:var(--green);color:var(--white);font-weight:700;font-size:13px;text-decoration:none;border-radius:2px}
.nav .btn{width:127px;height:40px;margin-left:-3px}
.eyebrow{left:0;width:1200px;display:flex;justify-content:center;align-items:center;gap:10px;font-weight:700;font-size:13px;letter-spacing:.6px;color:var(--green)}
.eyebrow::before,.eyebrow::after{content:"";width:108px;height:1px;background:var(--green)}
.hero .eyebrow{color:var(--white)}
.hero .eyebrow::before,.hero .eyebrow::after{background:rgba(255,255,255,.7)}
.title{left:0;width:1200px;text-align:center;font-weight:800;text-transform:uppercase}
.hero-title{top:266px;font-size:45px;line-height:55px;color:var(--white)}
.hero-sub{top:388px;left:280px;width:640px;text-align:center;color:var(--white);font-size:13.5px;line-height:21px}
.scroll{left:565px;top:520px}
.sec-title{font-size:28px;line-height:33px}
.card{top:790px;width:288px;height:306px;background:var(--white);box-shadow:0 2px 12px rgba(0,0,0,.07);padding:40px 30px 0}
.card svg{height:46px;display:block}
.card h3{font-size:18px;font-weight:800;line-height:21px;height:42px;margin-top:30px;display:flex;align-items:center;text-transform:uppercase}
.card p{font-size:14px;line-height:21px;color:var(--body);margin-top:20px}
.about{left:141px;top:1162px;width:912px;height:587px;background:var(--mint)}
.about-text{left:195px;top:1338px;width:410px;font-size:14px;line-height:22.5px;color:var(--body)}
.about-text p+p{margin-top:22px}
.about-img{left:626px;top:1342px;width:373px;height:342px;background:radial-gradient(circle at 50% 50%,#4bb6e6 0%,#14577f 30%,#0b2640 70%,#071626 100%)}
.about .btn,.about-btn{left:195px;top:1642px;width:167px;height:40px;position:absolute}
.field{position:absolute;border:1px solid var(--line);background:var(--white);font-size:12px;color:#444;padding:0 16px;display:flex;align-items:center}
.field.msg{align-items:flex-start;padding-top:16px}
.footer{left:0;top:2315px;width:1200px;height:169px;background:var(--mint)}
.social{left:0;width:1200px;top:2347px;display:flex;justify-content:center;gap:8px}
.social span{width:38px;height:38px;border:1.5px solid var(--green);border-radius:50%}
.foot-links{left:0;width:1200px;top:2400px;display:flex;justify-content:center;gap:30px;font-size:15.5px;color:var(--body)}
.copy{left:0;width:1200px;top:2433px;text-align:center;font-size:15px;color:var(--body)}
</style>
</head>
<body>
<header class="abs hero" role="img" aria-label="Photo of a researcher in a lab coat using a tablet in front of holographic data dashboards, dark teal tone">
</header>
<div class="abs brand"><span class="brand-dot"></span>FERNPATH HEALTH</div>
<nav class="abs nav">
  <a href="#">HOME</a><a href="#">SOLUTIONS</a><a href="#">ABOUT US</a><a class="btn" href="#">CONTACT US</a>
</nav>
<div class="abs eyebrow" style="top:238px">HEALTHCARE SOFTWARE SOLUTIONS</div>
<h1 class="abs title hero-title">Better care experiences,<br>improved cost savings</h1>
<p class="abs hero-sub">Automate processes, enable data-driven decisions, and expand innovation while ensuring minimal risks, redundancies, and costs.</p>
<svg class="abs scroll" width="70" height="70" viewBox="0 0 70 70" aria-label="Scroll for more">
  <circle cx="35" cy="35" r="33" fill="none" stroke="#fff" stroke-width="1" stroke-dasharray="2 3"/>
  <path d="M35 22v24M29 40l6 6 6-6" fill="none" stroke="#fff" stroke-width="1.5"/>
</svg>

<div class="abs eyebrow" style="top:701px">OUR SOLUTION</div>
<h2 class="abs title sec-title" style="top:723px">Innovative solutions in healthcare</h2>

<article class="abs card" style="left:141px">
  <svg viewBox="0 0 50 46" fill="none" stroke="#00AB8E" stroke-width="1.6"><rect x="1" y="1" width="44" height="40" rx="2"/><path d="M1 9h44"/><circle cx="26" cy="26" r="6"/><circle cx="26" cy="26" r="10" stroke-dasharray="3 2"/></svg>
  <h3>Custom software development</h3>
  <p>Lorem ipsum dolor sit amet, consectetur adipiscing elit. Aliquam rutrum nulla ac interdum tempus. Pellentesque ex justo.</p>
</article>
<article class="abs card" style="left:452px">
  <svg viewBox="0 0 50 46" fill="none" stroke="#00AB8E" stroke-width="1.6"><ellipse cx="34" cy="7" rx="12" ry="5"/><path d="M22 7v20c0 3 5 5 12 5s12-2 12-5V7M22 17c0 3 5 5 12 5s12-2 12-5"/><path d="M3 20l12-5 12 5v10c0 8-6 12-12 15C9 42 3 38 3 30z" fill="#fff"/></svg>
  <h3>Secure data storage</h3>
  <p>Lorem ipsum dolor sit amet, consectetur adipiscing elit. Aliquam rutrum nulla ac interdum tempus. Pellentesque ex justo.</p>
</article>
<article class="abs card" style="left:763px">
  <svg viewBox="0 0 54 46" fill="none" stroke="#00AB8E" stroke-width="1.6"><rect x="1" y="1" width="50" height="34" rx="2"/><path d="M8 28V20M14 28V14M20 28V18M38 20V8M44 20V12"/><circle cx="34" cy="28" r="8" fill="#fff"/><path d="M40 34l8 8"/></svg>
  <h3>Medical big data and analytics</h3>
  <p>Lorem ipsum dolor sit amet, consectetur adipiscing elit. Aliquam rutrum nulla ac interdum tempus. Pellentesque ex justo.</p>
</article>

<section class="abs about"></section>
<div class="abs eyebrow" style="top:1223px">ABOUT FERNPATH HEALTH</div>
<h2 class="abs title sec-title" style="top:1245px">Reducing human error, and lowering<br>costs through digital</h2>
<div class="abs about-text">
  <p>Moreover, the balance between cost and delivering positive patient experiences is fragile. Cost reduction strategies must prioritize the health of patients while examining opportunities to cut costs.</p>
  <p>The Fernpath Health eam of experts creates custom tailored healthcare management solutions. We design our systems with patients’ privacy, security, and the integrity of their health data in mind. Our healthcare management solutions can address the full range of healthcare workers’ needs regarding internal procedures, administrative tasks, and digital data management.</p>
</div>
<a class="btn about-btn" href="#">MORE ABOUT US</a>
<div class="abs about-img" role="img" aria-label="Finger touching a glowing cloud button surrounded by digital service icons"></div>

<div class="abs eyebrow" style="top:1810px">CONTACT US</div>
<h2 class="abs title sec-title" style="top:1832px">Let’s talk for lowest cost<br>healthcare coverage</h2>
<form>
  <div class="field" style="left:298px;top:1931px;width:287px;height:48px">Enter Your Full Name</div>
  <div class="field" style="left:610px;top:1931px;width:287px;height:48px">Enter Your Last Name</div>
  <div class="field" style="left:298px;top:2003px;width:287px;height:48px">Organization Name</div>
  <div class="field" style="left:610px;top:2003px;width:287px;height:48px">Enter Phone No.</div>
  <div class="field msg" style="left:298px;top:2075px;width:599px;height:112px">Write Your Message</div>
  <a class="btn abs" href="#" style="left:537px;top:2211px;width:127px;height:40px">CONTACT US</a>
</form>

<footer class="abs footer"></footer>
<div class="abs social" aria-label="Social links"><span></span><span></span><span></span><span></span></div>
<div class="abs foot-links"><span>Home</span><span>Solutions</span><span>About Us</span><span>Terms and Conditions</span><span>Privacy Policy</span></div>
<div class="abs copy">© 2022 Copyrights all reserved to Fernpath Health</div>
</body>
</html>
```